need eczema bath soak label/bag

need you to recreate this please. ai file. recreate this exact image please. ...if you want a big tip, create some different styles.

Colors
0054AA
0677BA
7BADD7
CADEEF
E8F1F8

```html
<!DOCTYPE html>
<html lang="en">
<head>
<meta charset="utf-8">
<title>Tidewell – The Ocean Healed My A Bag</title>
<link href="https://fonts.googleapis.com/css2?family=Barlow+Semi+Condensed:wght@600&family=Montserrat:wght@500;700&display=swap" rel="stylesheet">
<style>
  :root {
    --bg: #b9b9b5;
    --ink: #1f3a40;
    --sky-deep: #4f9cc4;
    --sky-mid: #7fc6d8;
    --sky-light: #cfe8ee;
    --sea-deep: #2fa7b5;
    --sea-light: #8fd6d2;
    --foam: #e8f4f2;
    --sand: #dcc6a0;
    --sand-dark: #cfb58a;
    --zip: rgba(255,255,255,0.45);
  }
  html, body {
    margin: 0;
    width: 1200px;
    height: 1108px;
    overflow: hidden;
    background: var(--bg);
  }
  .canvas {
    position: relative;
    width: 1200px;
    height: 1108px;
  }
  .pouch-front {
    position: absolute;
    left: 300px;
    top: 177px;
    width: 600px;
    height: 754px;
    overflow: hidden;
  }
  .scene-art {
    position: absolute;
    inset: 0;
    background: linear-gradient(to bottom,
      var(--sky-deep) 0%,
      var(--sky-mid) 18%,
      var(--sky-light) 42%,
      var(--sky-mid) 58%,
      var(--sea-deep) 61%,
      var(--sea-light) 70%,
      var(--foam) 75%,
      var(--sand) 78%,
      var(--sand-dark) 100%);
  }
  .zip-track {
    position: absolute;
    left: 0;
    right: 0;
    top: 88px;
    height: 8px;
    border-top: 2px solid var(--zip);
    border-bottom: 2px solid var(--zip);
  }
  .brand {
    position: absolute;
    left: 0;
    right: 0;
    top: 150px;
    text-align: center;
    color: var(--ink);
  }
  .brand-dot {
    display: block;
    width: 44px;
    height: 44px;
    margin: 0 auto 30px;
    border-radius: 50%;
    background: var(--ink);
  }
  .brand-name {
    font-family: "Barlow Semi Condensed", sans-serif;
    font-weight: 600;
    font-size: 22px;
    letter-spacing: 4px;
  }
  .headline {
    position: absolute;
    left: 0;
    right: 0;
    top: 288px;
    margin: 0;
    text-align: center;
    font-family: "Barlow Semi Condensed", sans-serif;
    font-weight: 600;
    font-size: 60px;
    line-height: 66px;
    color: var(--ink);
    letter-spacing: 0.5px;
  }
  .details {
    position: absolute;
    left: 0;
    right: 0;
    top: 602px;
    text-align: center;
    color: var(--ink);
    font-family: "Montserrat", sans-serif;
  }
  .details-copy {
    margin: 0 auto;
    width: 330px;
    font-size: 8.5px;
    line-height: 12px;
    font-weight: 500;
    text-transform: uppercase;
  }
  .details-tag {
    margin: 12px 0 0;
    font-size: 12px;
    font-weight: 700;
    letter-spacing: 1px;
  }
  .details-code {
    margin: 6px 0 0;
    font-family: "Barlow Semi Condensed", sans-serif;
    font-weight: 600;
    font-size: 19px;
    letter-spacing: 1px;
  }
  .details-note {
    margin: 4px 0 0;
    font-size: 8px;
    font-weight: 500;
    letter-spacing: 1px;
  }
</style>
</head>
<body>
<main class="canvas">
  <section class="pouch-front">
    <div class="scene-art" role="img" aria-label="Watercolour beach scene: blue sky with white clouds, turquoise sea and sandy shore"></div>
    <div class="zip-track"></div>
    <div class="brand">
      <span class="brand-dot"></span>
      <span class="brand-name">TIDEWELL</span>
    </div>
    <h1 class="headline">THE OCEAN<br>HEALED<br>MY A BAG</h1>
    <div class="details">
      <p class="details-copy">Lorem ipsum dolor sit amet, consectetuer adipiscing elit, sed diam nonummy nibh euismod tincidunt ut laoreet dolore magna aliquam erat volutpat.</p>
      <p class="details-tag">OCEAN | IN A BAG</p>
      <p class="details-code">B77 6.1119</p>
      <p class="details-note">SEA SOAK</p>
    </div>
  </section>
</main>
</body>
</html>
```